Business Card Design Project

need some business cards with the logo provided. I am a manufacturing jeweller that make high end quality jewellery in silver, gold and platinum and some amazing colored stones and of course diamonds.
Updates

Project Deadline Extended
Reason: I didn't choose this specific deadline and not sure why it was so short. A team member of craft huddle helped as i am not the best on computers. (-: (wasn't asked about the dead line)

Target Market(s)

Adults based between 20 to 60 and have budgets between $5000 - $100 000

Industry/Entity Type

Business

Colors

Designer to choose colors to be used in the design.

Requirements
Must have
• All in the front of business card
LOGO provided
My name: Corinne Walbeck
Job: Manufacturing jeweller
Phone number: 047 215 3904
Email: walcor@fernmail.example and the pagewave logo
this all in the back:
description of what i do : Hand Made Jewellery
new designs, remodelling, bridal jewellery, pearl re-threading and repairs
PO Box 1735, Marrindale, 6291
Should not have
• Any diamond shapes or diamond rings or gemstones.

```html
<!DOCTYPE html>
<html lang="en">
<head>
<meta charset="utf-8">
<title>Tallis Jewellers – Business Card</title>
<link rel="stylesheet" href="https://fonts.googleapis.com/css2?family=Tinos:wght@400&display=swap">
<style>
  :root {
    --backdrop: #ece7dc;
    --gold-light: #cdae45;
    --gold: #bf9d2e;
    --gold-deep: #b08e24;
    --brown: #4a1913;
    --card-w: 340px;
    --card-h: 580px;
  }
  * { box-sizing: border-box; margin: 0; padding: 0; }
  html, body {
    width: 1200px;
    height: 675px;
    overflow: hidden;
    background: var(--backdrop);
    font-family: "Tinos", "Times New Roman", serif;
  }
  .stage {
    width: 1200px;
    height: 675px;
    display: flex;
    align-items: center;
    justify-content: center;
    gap: 80px;
  }
  .card {
    position: relative;
    width: var(--card-w);
    height: var(--card-h);
    background: linear-gradient(160deg, var(--gold-light) 0%, var(--gold) 55%, var(--gold-deep) 100%);
    color: var(--brown);
    box-shadow: 0 10px 30px rgba(60, 40, 10, 0.25);
    display: flex;
    flex-direction: column;
    align-items: center;
  }
  .brand {
    margin-top: 44px;
    text-align: center;
    color: var(--brown);
  }
  .brand-name {
    display: block;
    font-size: 46px;
    letter-spacing: 8px;
    line-height: 1;
  }
  .brand-trade {
    display: block;
    margin-top: 8px;
    font-size: 15px;
    letter-spacing: 6px;
  }
  .flourish {
    margin-top: 18px;
    width: 120px;
    height: 42px;
    border-radius: 20px;
    background: radial-gradient(ellipse at center, rgba(74, 25, 19, 0.55), rgba(74, 25, 19, 0.12) 70%, transparent);
  }
  .holder-name {
    margin-top: 20px;
    font-size: 31px;
    font-weight: 400;
    letter-spacing: 0.5px;
  }
  .holder-role {
    margin-top: 2px;
    font-size: 20px;
  }
  .contact-list {
    list-style: none;
    width: 100%;
    margin-top: 30px;
    padding: 0 26px;
    display: flex;
    flex-direction: column;
    gap: 16px;
  }
  .contact-bar {
    height: 54px;
    background: var(--brown);
    color: var(--gold-light);
    display: flex;
    align-items: center;
    gap: 16px;
    padding: 0 16px;
    font-size: 20px;
    letter-spacing: 0.5px;
  }
  .contact-bar svg { flex: none; }
  .contact-email .contact-text { font-size: 18px; white-space: nowrap; }
  .social-mark {
    width: 26px;
    height: 26px;
    background: var(--gold-light);
    flex: none;
  }
  .services {
    list-style: none;
    margin-top: 28px;
    text-align: center;
    font-size: 22px;
    line-height: 1.22;
    letter-spacing: 0.5px;
  }
  .address-panel {
    position: absolute;
    left: 26px;
    right: 26px;
    bottom: 40px;
    height: 130px;
    background: var(--brown);
    color: var(--gold-light);
    display: flex;
    flex-direction: column;
    align-items: center;
    justify-content: center;
    gap: 14px;
  }
  .address-text {
    font-style: normal;
    font-size: 18px;
    letter-spacing: 0.5px;
    white-space: nowrap;
  }
</style>
</head>
<body>
<main class="stage">

  <section class="card card-front" aria-label="Card front">
    <div class="brand">
      <span class="brand-name">TALLIS</span>
      <span class="brand-trade">JEWELLERS</span>
    </div>
    <div class="flourish" role="img" aria-label="Decorative swirling flourish ornament"></div>
    <h1 class="holder-name">Corinne Walbeck</h1>
    <p class="holder-role">Manufacturing Jeweller</p>
    <ul class="contact-list">
      <li class="contact-bar contact-phone">
        <svg width="26" height="26" viewBox="0 0 24 24" aria-hidden="true">
          <path fill="#cdae45" d="M6.6 10.8c1.4 2.8 3.8 5.1 6.6 6.6l2.2-2.2c.3-.3.7-.4 1-.2 1.1.4 2.3.6 3.6.6.6 0 1 .4 1 1V20c0 .6-.4 1-1 1C10.6 21 3 13.4 3 4c0-.6.4-1 1-1h3.5c.6 0 1 .4 1 1 0 1.3.2 2.5.6 3.6.1.3 0 .7-.2 1z"/>
        </svg>
        <span class="contact-text">047 215 3904</span>
      </li>
      <li class="contact-bar contact-email">
        <svg width="28" height="22" viewBox="0 0 28 22" aria-hidden="true">
          <rect x="1" y="1" width="26" height="20" fill="#cdae45"/>
          <path d="M2 2 L14 12 L26 2" fill="none" stroke="#4a1913" stroke-width="2.2"/>
        </svg>
        <span class="contact-text">walcor@fernmail.example</span>
      </li>
      <li class="contact-bar contact-social">
        <span class="social-mark" aria-hidden="true"></span>
        <span class="contact-text">pagewave</span>
      </li>
    </ul>
  </section>

  <section class="card card-back" aria-label="Card back">
    <div class="brand">
      <span class="brand-name">TALLIS</span>
      <span class="brand-trade">JEWELLERS</span>
    </div>
    <ul class="services">
      <li>Hand Made Jewellery</li>
      <li>New Designs</li>
      <li>Remodelling</li>
      <li>Bridal Jewellery</li>
      <li>Pearl re-threading</li>
      <li>and</li>
      <li>Repairs</li>
    </ul>
    <div class="address-panel">
      <svg width="22" height="30" viewBox="0 0 22 30" aria-hidden="true">
        <path fill="#cdae45" d="M11 0C4.9 0 0 4.9 0 11c0 8 11 19 11 19s11-11 11-19C22 4.9 17.1 0 11 0zm0 15a4 4 0 1 1 0-8 4 4 0 0 1 0 8z"/>
      </svg>
      <address class="address-text">PO Box 1735, Marrindale, 6291</address>
    </div>
  </section>

</main>
</body>
</html>
```